Multi-Faceted Legal and Finanacial Advisory Group Needs Business Card Design

We need a business card design for a newly branded Orlando Florida area advising group consisting of Attorneys, Accountants and Financial Planners. The company is named RT Counsel Group. You will find our initial work on a business card. The information on the business card are merely guideposts and not final product. The logo does not have the be the same as provided since we have not finalized the logo. We would like to stay with a black/white/grey color scheme, but limited use of color is not out of the question.

Target Market(s)

Businesses and their Corporate Representatives

Industry/Entity Type

Business

Contact Information for Business Card

Should have Name, Title, Phone, Cell, Fax, Email and website. Logo should incorporate RT in some fashion however final logo used does not have to be the one on the document provided.

Requirements
Must have
• An RT design on front and back.

```html
<!DOCTYPE html>
<html lang="en">
<head>
<meta charset="utf-8">
<title>RT Counsel Group — Business Card</title>
<link rel="stylesheet" href="https://fonts.googleapis.com/css2?family=Tinos:ital,wght@0,400;0,700;1,400&display=swap">
<style>
  :root {
    --backdrop: #d9d9d9;
    --card-light: #ececec;
    --ink: #0c0c0c;
    --paper-text: #f4f4f4;
    --shadow: rgba(0,0,0,0.18);
  }
  * { margin: 0; padding: 0; box-sizing: border-box; }
  html, body {
    width: 1200px; height: 897px; overflow: hidden;
    background: var(--backdrop);
    font-family: "Tinos", "Times New Roman", serif;
  }
  .sheet {
    width: 1200px; height: 897px;
    display: flex; flex-direction: column; align-items: center; justify-content: center; gap: 60px;
  }
  .card {
    position: relative; width: 640px; height: 366px;
    background: var(--card-light); overflow: hidden;
    box-shadow: 0 6px 18px var(--shadow);
  }
  .card-shape { position: absolute; inset: 0; width: 100%; height: 100%; }

  /* Front */
  .front-brand {
    position: absolute; left: 165px; top: 70px;
    display: flex; align-items: center; gap: 18px;
  }
  .brand-square {
    flex: none;
    width: 66px; height: 66px; background: var(--ink);
    outline: 3px solid var(--card-light); outline-offset: -9px;
    border: 2px solid var(--card-light);
  }
  .brand-text { display: flex; flex-direction: column; }
  .brand-name { font-size: 40px; color: var(--ink); line-height: 1; }
  .brand-tagline { font-size: 11px; color: var(--ink); margin-top: 6px; letter-spacing: 0.3px; }

  /* Back */
  .back-brand {
    position: absolute; right: 36px; top: 44px;
    display: flex; align-items: center; gap: 14px;
  }
  .back-brand .brand-square { width: 96px; height: 96px; outline-offset: -12px; }
  .back-brand .brand-name { font-size: 30px; width: 150px; line-height: 1.1; }
  .contact {
    position: absolute; left: 40px; top: 148px;
    color: var(--paper-text); font-size: 14.5px; line-height: 1.38;
  }
  .contact-name { font-weight: 700; font-size: 16px; }
  .contact-title { font-style: italic; }
  .website {
    position: absolute; left: 40px; bottom: 26px;
    color: var(--paper-text); font-size: 27px; line-height: 1.1;
  }
</style>
</head>
<body>
<main class="sheet">
  <section class="card card-front" aria-label="Card front">
    <svg class="card-shape" viewBox="0 0 640 366" preserveAspectRatio="none" aria-hidden="true">
      <polygon points="0,0 130,0 350,366 0,366" fill="var(--ink)"/>
    </svg>
    <div class="front-brand">
      <div class="brand-square" aria-hidden="true"></div>
      <div class="brand-text">
        <span class="brand-name">RT Counsel Group</span>
        <span class="brand-tagline">Attorneys • Accountants • Financial Planners</span>
      </div>
    </div>
  </section>

  <section class="card card-back" aria-label="Card back">
    <svg class="card-shape" viewBox="0 0 640 366" preserveAspectRatio="none" aria-hidden="true">
      <polygon points="0,0 250,0 380,150 640,230 640,366 0,366" fill="var(--ink)"/>
    </svg>
    <div class="back-brand">
      <div class="brand-square" aria-hidden="true"></div>
      <span class="brand-name">RT Counsel Group</span>
    </div>
    <div class="contact">
      <div class="contact-name">Daniel K. Moreau, Esq.</div>
      <div class="contact-title">Attorney</div>
      <div>2260 Harbor Point Drive, Suite 410</div>
      <div>Winter Park, FL 32789</div>
      <div>Off: (407) 555-0142</div>
      <div>Cell: (407) 555-0187</div>
      <div>Email: dmoreau@rt-counsel.com</div>
    </div>
    <div class="website">Web: www.rt-counsel.com</div>
  </section>
</main>
</body>
</html>
```